This is for a plastic credit card type business card for handing out to clients. It only has the web

I'm looking for a two sided card. This will be printed on a credit card type plastic, ie rounded edges. On the one side is the design. On the other 10 Codes.

The front. A design that is funky but still appropriate for someone in their 30's to 60's The words "Entrepreneurs Code" "Dorin Malcove" must appear on the front. At the bottom in small writing (Portrait) is www.vestobiq.com

So I'm really looking for the design of the top of the card in making my decision.

On the back of the card in portrait is the following copy.

Heading in Bold is "Entrepreneurs Code"

I will always remember my WHY
I am an agent for growth and prosperity
I really deserve success in my life
I always stand up again
I will reach out for support on my journey
I will lend fellow entrepreneurs support on their journey
I have the gift of a flexible mind
I see opportunity where others don't
I use my fears to drive me forward
I see success and failure as a learning opportunity

AT THE BOTTOM OF BACK OF THE CARD IS

www.vestobiq.com

```html
<!DOCTYPE html>
<html lang="en">
<head>
<meta charset="utf-8">
<title>Entrepreneurs Code – Business Card</title>
<link rel="stylesheet" href="https://fonts.googleapis.com/css2?family=Cabin:wght@400;600;700&display=swap">
<style>
  :root {
    --canvas-bg: #e4e3de;
    --card-light: #f7f8f9;
    --card-shade: #dfe2e5;
    --ink: #1f1f21;
    --ink-soft: #3a3b3e;
    --blue-bright: #4ed6f2;
    --blue-mid: #2fa9e0;
    --blue-deep: #1e8dcc;
    --card-radius: 18px;
  }
  * { box-sizing: border-box; margin: 0; padding: 0; }
  html, body {
    width: 900px;
    height: 1200px;
    overflow: hidden;
  }
  body {
    background: var(--canvas-bg);
    font-family: "Cabin", "Gill Sans", sans-serif;
    color: var(--ink);
    position: relative;
  }
  .card {
    position: absolute;
    top: 300px;
    width: 380px;
    height: 600px;
    border-radius: var(--card-radius);
    overflow: hidden;
    background: linear-gradient(160deg, var(--card-light) 0%, #eef0f2 55%, var(--card-shade) 100%);
    box-shadow: 0 14px 30px rgba(0, 0, 0, 0.18), 0 2px 5px rgba(0, 0, 0, 0.12);
  }
  .card--front { left: 50px; }
  .card--back  { left: 470px; background: #ffffff; }

  .front__art {
    position: absolute;
    top: 130px;
    left: 0;
    right: 0;
    height: 420px;
    background: linear-gradient(160deg, var(--blue-bright) 0%, var(--blue-mid) 50%, var(--blue-deep) 100%);
  }
  .front__title {
    position: absolute;
    top: 72px;
    left: 0;
    right: 0;
    text-align: center;
    font-size: 29px;
    font-weight: 700;
    letter-spacing: 0.2px;
  }
  .front__name {
    position: absolute;
    top: 290px;
    left: 0;
    right: 0;
    text-align: center;
    font-weight: 700;
    color: var(--ink);
  }
  .front__name-line {
    display: block;
    font-size: 31px;
    line-height: 1.1;
  }
  .front__role {
    display: block;
    font-size: 25px;
    font-weight: 600;
    margin-top: 6px;
  }
  .card__url {
    position: absolute;
    bottom: 18px;
    left: 0;
    right: 0;
    text-align: center;
    font-size: 13px;
    font-weight: 700;
    color: var(--ink);
  }

  .back__title {
    position: absolute;
    top: 44px;
    left: 24px;
    font-size: 28px;
    font-weight: 700;
  }
  .code-list {
    position: absolute;
    top: 112px;
    left: 24px;
    right: 18px;
    list-style: none;
  }
  .code-list__item {
    font-size: 11.5px;
    line-height: 1;
    white-space: nowrap;
    color: var(--ink-soft);
    margin-bottom: 26px;
  }
</style>
</head>
<body>

  <section class="card card--front" aria-label="Card front">
    <div class="front__art" role="img" aria-label="Abstract blue geometric artwork"></div>
    <h1 class="front__title">Entrepreneurs Code</h1>
    <p class="front__name">
      <span class="front__name-line">Dorin Malcove</span>
      <span class="front__role">C.E.O.</span>
    </p>
    <p class="card__url">www.vestobiq.com</p>
  </section>

  <section class="card card--back" aria-label="Card back">
    <h2 class="back__title">Entrepreneurs Code</h2>
    <ul class="code-list">
      <li class="code-list__item">I will always remember my WHY</li>
      <li class="code-list__item">I am an agent for growth and prosperity</li>
      <li class="code-list__item">I really deserve success in my life</li>
      <li class="code-list__item">I always stand up again</li>
      <li class="code-list__item">I will reach out for support on my journey</li>
      <li class="code-list__item">I will lend fellow entrepreneurs support on their journey</li>
      <li class="code-list__item">I have the gift of a flexible mind</li>
      <li class="code-list__item">I see opportunity where others don't</li>
      <li class="code-list__item">I use my fears to drive me forward</li>
      <li class="code-list__item">I see success and failure as a learning opportunity</li>
    </ul>
    <p class="card__url">www.vestobiq.com</p>
  </section>

</body>
</html>
```